Wordpress Template für Weinkommunikation
Zielgruppe
Kunden und potentielle Kunden, die sich über meine Dienstleistungen und mich informieren wollen.
Meine Arbeitsschwerpunkte sind Kommunikation, PR und Events im Weinbereich.
Meine persönlichen Wein-Schwerpunktländer sind Spanien und Portugal. Die Kunden sind von dort, meine Arbeit ist in Deutschland.
Aufgabenstellung
Ich möchte meine bestehende Website endlich mal richtig gestalten lassen.
- Startseite soll statisch sein.
- Weitere Seiten sollen auch statisch möglich sein.
- 2- oder 3-spaltig
- Template muss Widget-fähig sein
- Möglichkeit der Zweisprachigkeit

```html
<!DOCTYPE html>
<html lang="de">
<head>
<meta charset="utf-8">
<title>Eine Woche in Brasilien – Rebe &amp; Kunde</title>
<link href="https://fonts.googleapis.com/css2?family=Gelasio:wght@400;700&family=Open+Sans:wght@400;600;700&display=swap" rel="stylesheet">
<style>
:root{
  --page-bg:#f3e6cc;
  --paper:#fdf8ec;
  --header:#ffffff;
  --band:#4e2a14;
  --band-hi:#7a4a2a;
  --ink:#2b1a10;
  --muted:#8a7a66;
  --accent:#d8881a;
  --link:#e6a412;
  --tag:#5a8fb4;
  --name:#8c1414;
  --box-line:#e0c58f;
  --box-bg:#fff9e8;
  --field:#ede0c2;
  --kraft:#c7a77a;
  --wine:#9a1020;
}
*{box-sizing:border-box;margin:0;padding:0}
html,body{width:1187px;height:1200px;overflow:hidden}
body{background:linear-gradient(180deg,var(--page-bg),#f7ecd6 60%,var(--page-bg));font-family:"Gelasio",Georgia,serif;color:var(--ink);position:relative}
.canvas{position:absolute;left:51px;top:0;width:1089px;height:1200px;background:var(--paper)}
.abs{position:absolute}
.site-header{left:0;top:0;width:1089px;height:117px;background:var(--header)}
.brand{left:30px;top:34px;display:flex;align-items:center;gap:12px;font-weight:700;font-size:34px;color:var(--name)}
.brand-mark{width:22px;height:22px;background:var(--accent)}
.social{top:38px;width:58px;height:58px;border-radius:10px}
.social.one{left:925px;background:#5bb8e6}
.social.two{left:1005px;background:#ef8a24}
.band{left:0;top:117px;width:1089px;height:40px;background:linear-gradient(90deg,var(--band),var(--band-hi) 50%,var(--band))}
.band span{position:absolute;left:66px;top:10px;color:#d8c3a0;font-size:17px}
.footer-band{left:0;top:1170px;width:1089px;height:30px;background:linear-gradient(90deg,var(--band),var(--band-hi) 50%,var(--band))}
.post-title{left:-18px;top:214px;width:711px;height:50px;background:linear-gradient(180deg,#f1e4c6,#e8d6ae)}
.post-date{left:69px;top:10px;text-align:center;line-height:1}
.post-date b{display:block;font-size:22px}
.post-date small{font-family:"Open Sans",sans-serif;font-size:11px;color:var(--accent)}
.post-title h1{position:absolute;left:129px;top:12px;font-weight:400;font-size:22px;color:#3a2414}
.post-body{left:68px;top:287px;width:548px;font-size:15.5px;line-height:20px}
.post-body p{margin-bottom:20px}
.post-body a{color:var(--accent);text-decoration:none}
.map{left:66px;top:456px;width:250px;height:361px;border:2px solid #e8c88c;background:linear-gradient(135deg,#8fc2e4,#6aa8d6 55%,#e7874a 70%,#f0c98a)}
.post-aside{left:343px;top:456px;width:290px;font-size:15.5px;line-height:20px}
.post-aside p{margin-bottom:20px}
.post-meta{left:70px;top:841px;font-family:"Open Sans",sans-serif;font-size:10px;letter-spacing:1px;text-transform:uppercase;color:var(--muted);font-style:italic}
.post-meta .tags{margin-top:8px;padding-left:44px;font-weight:700}
.post-meta .tags a{color:var(--tag);text-decoration:none}
.comment-head{left:76px;top:903px;font-size:14px}
.comment-field{left:66px;top:933px;width:564px;height:91px;background:var(--field);border:2px solid #e6cf9c}
.btn{top:1038px;height:29px;background:linear-gradient(90deg,#e4cfa4,#f1e4c6);font-size:14px;padding:5px 0 0 32px}
.btn.create{left:66px;width:197px}
.btn.preview{left:280px;width:131px}
.note{left:683px;top:142px;width:334px;height:130px;background:var(--kraft);transform:rotate(-3deg);display:flex;align-items:center;justify-content:space-around;padding:0 30px;font-family:"Open Sans",sans-serif;font-size:13px;color:#6a4c2c;letter-spacing:2px}
.box{left:675px;width:383px;background:var(--box-bg);border:1px solid var(--box-line)}
.box h2{font-weight:400;font-size:17px;margin:16px 0 0 20px}
.about{top:306px;height:154px}
.portrait{left:20px;top:44px;width:88px;height:88px;background:linear-gradient(180deg,#d9dde2,#5a5e66);border:1px solid #d8c08a}
.about-text{left:128px;top:42px;width:240px;font-size:13.5px;line-height:18px}
.about-text b{color:var(--name)}
.about-text span{color:var(--link)}
.badge-blog{top:482px;height:82px}
.badge-blog i{position:absolute;left:22px;top:18px;width:185px;height:50px;background:#111;border-radius:6px 24px 24px 6px}
.tweets{top:590px;height:157px}
.tweets ul{margin:14px 20px 0 22px;list-style:none;font-size:13.5px;line-height:16px}
.tweets li{padding-left:20px;position:relative}
.tweets li::before{content:"";position:absolute;left:0;top:5px;width:7px;height:7px;background:#b8a98a}
.tweets em{font-style:normal;color:var(--link)}
.badge-moderation{left:676px;top:774px;width:383px;height:50px;border:1px solid #9a8a8a;background:#fff}
.badge-moderation i{position:absolute;left:12px;top:12px;width:24px;height:24px;border-radius:50%;background:var(--wine)}
.member{top:849px;height:230px}
.member i{position:absolute;left:10px;top:14px;width:238px;height:200px;background:#fff;border-top:3px solid #f6f0e6}
.footer-links{left:68px;top:1138px;font-family:"Open Sans",sans-serif;font-size:12px;color:#8a6a3a}
.footer-brand{left:936px;top:1124px;font-weight:700;font-size:18px;color:var(--name)}
</style>
</head>
<body>
<div class="canvas">
  <header class="abs site-header">
    <div class="abs brand"><span class="brand-mark"></span>Rebe &amp; Kunde</div>
    <span class="abs social one" aria-label="Kurznachrichten"></span>
    <span class="abs social two" aria-label="Feed"></span>
  </header>
  <div class="abs band"><span>blog.rebenkunde.de</span></div>

  <div class="abs post-title">
    <div class="abs post-date"><b>01</b><small>NOV</small></div>
    <h1>Eine Woche in Brasilien</h1>
  </div>

  <div class="abs post-body">
    <p>Auf Einladung von <a href="#">“Vinhos do Sul”</a> habe ich mir eine Woche lang den Weinbau im Süden von Brasilien angesehen. Eine ganz neue Erfahrung für mich. Das, was ich als “typisch Brasilianisch” im Kopf hatte, habe ich so gut wie nicht gesehen. Dafür vieles andere, was mich fasziniert hat.</p>
    <p>Zunächst musste ich mir erst einmal der Dimension des Landes Brasilien bewusst werden …</p>
  </div>

  <div class="abs map" role="img" aria-label="Landkarte Südamerikas mit Brasilien hervorgehoben"></div>
  <div class="abs post-aside">
    <p>Man kann sich das Land ungefähr als Dreieck vorstellen. Die größte Aus&shy;dehnung von Nord nach Süd beträgt rund 4.200 km. Fast ebenso groß ist die Ost-West Ausdehnung. Wenn man die nördliche Spitze auf London legt, ist der südlichste Punkt in Zentralafri&shy;ka.</p>
    <p>Der Inlandsflug von Rio de Janeiro nach Porto Alegre dauert 2,5 Stunden und ist mit einem Flug von Köln nach Madrid vergleichbar. Bei einer Fläche von über 8,5 Millionen km² (24 mal so groß wie Deutschland), bedeckt Brasilien fast die Hälfte des südameri&shy;kanischen Kontinents.</p>
  </div>

  <div class="abs post-meta">
    <div>Eingestellt von qaswert am 31.8.10</div>
    <div class="tags">Tags: <a href="#">Brasilien</a>, <a href="#">Rebsorten</a>, <a href="#">Reisen</a>, <a href="#">Wein</a></div>
  </div>

  <div class="abs comment-head">Kommentar veröffentlichen</div>
  <div class="abs comment-field"></div>
  <div class="abs btn create">Kommentar erstellen</div>
  <div class="abs btn preview">Vorschau</div>

  <div class="abs note"><span>RSS FEED</span><span>EMAIL UPDATES</span></div>

  <section class="abs box about">
    <h2>Über mich</h2>
    <div class="abs portrait" role="img" aria-label="Porträtfoto des Autors"></div>
    <div class="abs about-text"><b>Jens K. Marlow</b><br>Wein ist ein großer und wichtiger Bestandteil meines Lebens.<br><span>Mehr dazu auf meiner Website www.rebenkunde.de</span></div>
  </section>

  <section class="abs box badge-blog"><i aria-label="Blogverzeichnis-Abzeichen"></i></section>

  <section class="abs box tweets">
    <h2>Kurznachrichten</h2>
    <ul>
      <li>@rebhof Wann können wir das Ergebnis verkosten? #riesling <em>14 days ago</em></li>
      <li>Madeira-Verkostung in Hamburg http://kurz.li/4TrX9 <em>26 days ago</em></li>
      <li>Erste Einschätzung des Port-Jahrgangs 2010 http://kl.ink/PmQv7sLa <em>28 days ago</em></li>
    </ul>
  </section>

  <div class="abs badge-moderation" aria-label="Partnerabzeichen"><i></i></div>

  <section class="abs box member"><i aria-label="Mitgliedsabzeichen"></i></section>

  <nav class="abs footer-links">Kontakt | Impressum | Blog | Wein-Glossar | Adresse</nav>
  <div class="abs footer-brand">Traubennetz.de</div>
  <div class="abs footer-band"></div>
</div>
</body>
</html>
```